Business Sign

I need a business sign designed, based on the business card design/logo/font/colours I have previously had created by Artfolio. It is to be a window decal which will be affixed to the inside of my business window front. I will probably have it printed through Printavo. The largest size available through PrintAvo is 49 x 32.1cm therefore I would like a series of three signs that will be positioned down the front of my window.
Information I require on sign 1 includes:
business name and logo
phone number
web address
email address
Information I require on sign 2 includes:
Sewing Classes Beginner to Advanced
Social Sewing Classes
Pattern Fitting Classes
Pattern Drafting Classes
Information I require on sign 3 includes:
Alteration Services
Dressmaking Services
Auxiliary Services
As a suggestion, please view my website homepage on www.threadbloomstudio.com.au as the background dressmaking themed cliparts may provide some inspiration to "decorate" the signs.

Target Market(s)

For sewing classes:
predominately female, 18-65yo, stay-at-home mums, professional women seeking creative outlet, women wanting to sell on-line or at markets, young adults looking to enter the fashion industry, retired women sewing as a hobby, women with fitting issues who find it difficult to find clothes in shops
For alterations:
all age groups male and female

Industry/Entity Type

Business

Font styles to use
Other font styles liked:
• as per business card

Requirements
Must have
• must be similar to business card in style, font, colour, look etc......

```html
<!DOCTYPE html>
<html lang="en">
<head>
<meta charset="utf-8">
<title>Thread Bloom – Window Signs</title>
<link rel="stylesheet" href="https://fonts.googleapis.com/css2?family=Kalam:wght@400;700&family=Oswald:wght@400&display=swap">
<style>
  :root{
    --canvas:#fbeaf5;
    --card:#fcf4f8;
    --plum:#53404f;
    --pink:#f09cc4;
    --pink-text:#ea8fbd;
    --ink:#4a3646;
    --white:#ffffff;
    --form:#f6cde2;
    --form-soft:#dcc0d8;
    --pattern:#f3dde8;
  }
  *{box-sizing:border-box;margin:0;padding:0}
  html,body{width:1200px;height:1000px;overflow:hidden;background:var(--canvas)}
  .board{position:relative;width:1200px;height:1000px}
  .sign{position:absolute;width:446px;height:290px;background:linear-gradient(180deg,#fdfafc,var(--card));box-shadow:0 0 10px rgba(60,30,50,.55);overflow:hidden}
  .sign svg.art{position:absolute;inset:0;width:100%;height:100%}
  .sign--contact{left:88px;top:47px}
  .sign--classes{left:372px;top:357px}
  .sign--services{left:655px;top:672px}

  .notions{position:absolute;background:var(--pattern);
    -webkit-mask-image:radial-gradient(ellipse 50% 50% at 50% 50%,#000 30%,transparent 100%);
    mask-image:radial-gradient(ellipse 50% 50% at 50% 50%,#000 30%,transparent 100%);opacity:.8}

  .brand{position:absolute;left:130px;top:34px;font-family:"Kalam",cursive;font-weight:400;font-size:48px;color:var(--ink);line-height:1}
  .contact{position:absolute;right:12px;top:202px;list-style:none;font-family:"Oswald",sans-serif;font-size:15px;color:var(--pink-text);text-align:right}
  .contact li{display:flex;justify-content:flex-end;align-items:center;gap:7px;height:27px}
  .contact svg{width:16px;height:16px}

  .tab-name{position:absolute;left:268px;top:8px;width:100px;text-align:center;font-family:"Kalam",cursive;font-size:14px;color:var(--white)}
  .offer{position:absolute;list-style:none;font-family:"Oswald",sans-serif;font-size:21px;color:var(--pink-text)}
  .offer li{height:35.5px;display:flex;align-items:center}
  .offer li::before{content:"";width:7px;height:7px;border-radius:50%;background:var(--pink-text);margin-right:9px}
  .sign--classes .offer{left:12px;top:70px}
  .sign--services .offer{left:43px;top:86px}
  .offer--tight li::before{margin-right:5px}

  .tagline{position:absolute;left:94px;top:20px;font-family:"Kalam",cursive;font-size:16.5px;color:var(--ink)}
  .social{position:absolute;right:10px;bottom:6px;display:flex;align-items:center;gap:4px;font-family:"Oswald",sans-serif;font-size:10px;color:var(--white)}
  .social i{width:8px;height:8px;background:var(--pink)}
</style>
</head>
<body>
<main class="board">

  <!-- Sign 1: name and contact -->
  <section class="sign sign--contact">
    <svg class="art" viewBox="0 0 446 290" aria-hidden="true">
      <path d="M0,290 L0,274 C130,286 240,215 320,168 C370,138 415,120 446,118 L446,290 Z" fill="var(--plum)"/>
      <path d="M0,262 C110,288 230,240 320,175 C370,138 415,118 446,114 L446,122 C410,126 370,148 322,184 C230,250 110,296 0,282 Z" fill="var(--white)"/>
      <path d="M0,226 C90,262 200,250 300,190 C360,150 410,108 446,102 L446,112 C405,118 360,160 305,200 C210,258 100,282 0,246 Z" fill="var(--pink)"/>
    </svg>
    <div role="img" aria-label="Dressmaker's mannequin illustration with ribbon sash" style="position:absolute;left:34px;top:18px;width:84px;height:262px;border-radius:40px 40px 10px 10px;background:linear-gradient(180deg,var(--form),#e8b8d4 70%,#b07aa3)"></div>
    <div class="brand">Thread Bloom</div>
    <ul class="contact">
      <li>0400 128 976
        <svg viewBox="0 0 16 16"><path d="M2 6c0-3 12-3 12 0v1h-3V5.5C9 5 7 5 5 5.5V7H2z M4 8h8l2 6H2z" fill="var(--pink-text)"/></svg></li>
      <li>info@threadbloomstudio.com.au
        <svg viewBox="0 0 16 16"><rect x="1" y="3" width="14" height="10" fill="var(--pink-text)"/><path d="M1 3l7 6 7-6" fill="none" stroke="var(--plum)" stroke-width="1.2"/></svg></li>
      <li>www.threadbloomstudio.com.au
        <svg viewBox="0 0 16 16"><g fill="none" stroke="var(--pink-text)" stroke-width="1.3"><circle cx="8" cy="8" r="6.5"/><ellipse cx="8" cy="8" rx="3" ry="6.5"/><path d="M1.5 8h13M3 4.5h10M3 11.5h10"/></g></svg></li>
    </ul>
  </section>

  <!-- Sign 2: classes -->
  <section class="sign sign--classes">
    <div class="notions" role="img" aria-label="Faint pattern of sewing notions: buttons, spools, scissors, machines" style="left:-20px;top:110px;width:340px;height:170px"></div>
    <svg class="art" viewBox="0 0 446 290" aria-hidden="true">
      <path d="M0,0 H446 V18 H376 L370 30 Q368 33 364 33 H272 Q268 33 266 30 L262 18 H0 Z" fill="var(--plum)"/>
      <path d="M0,258 C120,290 240,250 330,180 C380,145 420,125 446,118 L446,128 C420,136 385,155 340,190 C250,262 120,300 0,282 Z" fill="var(--pink)"/>
      <path d="M0,268 C110,290 220,262 280,232 L280,238 C220,270 110,292 0,276 Z" fill="var(--pink)"/>
    </svg>
    <div role="img" aria-label="Tailor's dress form on a stand" style="position:absolute;left:356px;top:60px;width:50px;height:214px;border-radius:22px 22px 6px 6px;background:linear-gradient(180deg,var(--form-soft),#e6d2e2)"></div>
    <div class="tab-name">Thread Bloom</div>
    <ul class="offer">
      <li>Sewing Classes Beginner to Advanced</li>
      <li>Social Sewing Classes</li>
      <li>Pattern Fitting Classes</li>
      <li>Pattern Drafting Classes</li>
    </ul>
  </section>

  <!-- Sign 3: services -->
  <section class="sign sign--services">
    <div class="notions" role="img" aria-label="Faint pattern of sewing notions" style="left:-20px;top:120px;width:330px;height:150px"></div>
    <svg class="art" viewBox="0 0 447 290" aria-hidden="true">
      <line x1="0" y1="2" x2="447" y2="2" stroke="#b9a7b3" stroke-width="4" stroke-dasharray="6 3"/>
      <line x1="64" y1="63" x2="447" y2="63" stroke="#9a8794" stroke-width="1" stroke-dasharray="8 4"/>
      <path d="M0,268 C130,290 250,250 330,170 C370,132 410,115 447,108 L447,290 L0,290 Z" fill="var(--plum)"/>
      <path d="M0,254 C120,282 240,246 320,175 C365,135 410,112 447,104 L447,112 C410,120 370,142 328,182 C250,256 120,292 0,268 Z" fill="var(--white)"/>
      <path d="M0,228 C110,266 230,238 310,170 C360,128 410,106 447,100 L447,110 C410,116 365,138 318,180 C235,250 110,282 0,244 Z" fill="var(--pink)"/>
    </svg>
    <div role="img" aria-label="Scissors icon" style="position:absolute;left:24px;top:52px;width:40px;height:18px;border-radius:8px;background:var(--ink)"></div>
    <div role="img" aria-label="Dressmaker's mannequin illustration with ribbon sash" style="position:absolute;left:342px;top:52px;width:62px;height:196px;border-radius:30px 30px 8px 8px;background:linear-gradient(180deg,var(--form),#e8b8d4 70%,#8f4f80)"></div>
    <div class="tagline">The Art of Turning Fabric into Fashion</div>
    <ul class="offer offer--tight">
      <li>Alteration Services</li>
      <li>Dressmaking Services</li>
      <li>Auxiliary Services</li>
    </ul>
    <div class="social"><i></i>@threadbloom</div>
  </section>

</main>
</body>
</html>
```